Copper Ridge Technologies - Van Wrap

Project Overview
Copper Ridge Technologies is a fast-growing telecommunications company seeking a bold, professional van wrap design for our new fleet vehicle (Ford Transit 250 Cargo). The wrap should clearly communicate our brand identity, highlight our core services, and create strong brand visibility on the road.
Objectives
Design a full vehicle wrap for a Ford Transit 250 Cargo.
Establish instant brand recognition using our logo, brand colors, and clean design.
Communicate our core services in a clear, simple, and modern way.
Ensure the design is legible from a distance and looks professional across a fleet of vehicles.
Brand Identity
Company Name: Copper Ridge Technologies
Industry: Telecommunications / Low Voltage Solutions
Brand Attributes: Professional, Trustworthy, Innovative, Technical Expertise
Brand Colors: Blue, White, Grey (on a full black base)
Logo Files Provided: AI and PSD (attached)
Core Services to Highlight
Cameras
Access Control
Cabling & Networking
Audio / Visual
(We would like these paired with simple, modern icons for quick recognition.)
Van Content:
Should include the following:
Logo (attached)
Services:Cameras
Access Control
Cabling & Networking
Audio / Visual
Phone number: 800-362-5914
Website: www.copperridgenet.example

```html
<!DOCTYPE html>
<html lang="en">
<head>
<meta charset="utf-8">
<title>Copper Ridge Technologies – Van Wrap</title>
<link rel="stylesheet" href="https://fonts.googleapis.com/css2?family=Montserrat:wght@600&family=Exo+2:wght@800&family=Archivo+Black&display=swap">
<style>
  :root {
    --page: #ffffff;
    --body: #1f1f20;
    --body-edge: #111112;
    --blue: #3b8fe0;
    --blue-deep: #2a6fc4;
    --silver: #d9dde2;
    --glass: #c9cdd1;
    --tyre: #161616;
    --rim: #a9adb1;
    --ink: #111111;
    --white: #f4f4f4;
  }
  html, body { margin: 0; padding: 0; overflow: hidden; background: var(--page); }
  .canvas { width: 1200px; height: 821px; position: relative; overflow: hidden; }
  .canvas svg { display: block; }
  .van-body { fill: var(--body); stroke: var(--body-edge); stroke-width: 2; }
  .glass { fill: var(--glass); }
  .band-blue { fill: var(--blue); }
  .band-silver { fill: var(--silver); }
  .chip-blue { fill: var(--blue); }
  .chip-dark { fill: var(--ink); }
  .tyre { fill: var(--tyre); }
  .rim { fill: var(--rim); }
  .brand-name { font-family: "Montserrat", sans-serif; font-weight: 600; fill: var(--white); }
  .brand-mark { fill: var(--blue); }
  .services { font-family: "Exo 2", sans-serif; font-weight: 800; fill: var(--blue); }
  .contact { font-family: "Archivo Black", sans-serif; fill: var(--ink); }
</style>
</head>
<body>
<div class="canvas">
<svg width="1200" height="821" viewBox="0 0 1200 821" xmlns="http://www.w3.org/2000/svg">
  <defs>
    <g id="side-panel">
      <path class="van-body" d="M32,70 Q32,46 58,46 L505,48 Q560,52 600,90 L690,180 Q775,200 800,240 L808,292 Q808,320 788,322 L40,322 Q28,322 28,305 Z"/>
      <path class="glass" d="M525,108 L598,110 L658,182 L660,200 L525,198 Z"/>
      <path class="band-silver" d="M50,196 L500,196 Q566,198 594,276 L578,276 Q552,210 500,206 L50,206 Z"/>
      <path class="band-blue" d="M50,206 L500,206 Q550,212 574,276 L50,276 Z"/>
      <rect class="band-blue" x="235" y="300" width="338" height="11"/>
      <rect class="band-silver" x="578" y="300" width="12" height="11"/>
      <g class="chip-blue">
        <rect x="58" y="58" width="18" height="18"/><rect x="80" y="62" width="12" height="12"/>
        <rect x="96" y="54" width="10" height="10"/><rect x="110" y="58" width="8" height="8"/>
        <rect x="48" y="90" width="20" height="20"/><rect x="74" y="80" width="10" height="10"/>
        <rect x="94" y="72" width="10" height="10"/><rect x="76" y="98" width="10" height="12"/>
      </g>
      <g class="chip-dark">
        <rect x="58" y="210" width="22" height="22"/><rect x="86" y="212" width="10" height="10"/>
        <rect x="84" y="226" width="16" height="16"/><rect x="104" y="232" width="10" height="10"/>
        <rect x="68" y="244" width="20" height="18"/><rect x="96" y="250" width="12" height="12"/>
        <rect x="112" y="250" width="10" height="10"/><rect x="90" y="266" width="10" height="8"/>
        <rect x="108" y="266" width="12" height="8"/><rect x="124" y="268" width="8" height="6"/>
      </g>
      <circle class="tyre" cx="172" cy="326" r="46"/><circle class="rim" cx="172" cy="326" r="24"/>
      <circle class="tyre" cx="680" cy="326" r="46"/><circle class="rim" cx="680" cy="326" r="24"/>
    </g>
  </defs>

  <!-- Driver side -->
  <g class="side-view driver-side">
    <use href="#side-panel"/>
    <text class="brand-name" x="104" y="126" font-size="36">COPPER RIDGE</text>
    <text class="brand-name" x="106" y="148" font-size="12.5" letter-spacing="6.2">TECHNOLOGIES</text>
    <rect class="brand-mark" x="415" y="86" width="58" height="58"/>
    <text class="services" x="130" y="170" font-size="13">Cameras <tspan dx="4">▪</tspan><tspan dx="6">Access Control</tspan></text>
    <text class="services" x="90" y="186" font-size="13">Cabling &amp; Networking <tspan dx="4">▪</tspan><tspan dx="6">Audio / Visual</tspan></text>
    <text class="contact" x="112" y="228" font-size="11.5">www.copperridgenet.example</text>
    <text class="contact" x="312" y="256" font-size="24">800-362-5914</text>
  </g>

  <!-- Passenger side -->
  <g class="side-view passenger-side">
    <use href="#side-panel" transform="translate(830,400) scale(-1,1)"/>
    <rect class="brand-mark" x="372" y="486" width="58" height="58"/>
    <text class="brand-name" x="448" y="530" font-size="36">COPPER RIDGE</text>
    <text class="brand-name" x="450" y="552" font-size="12.5" letter-spacing="6.2">TECHNOLOGIES</text>
    <text class="services" x="495" y="572" font-size="13">Cameras <tspan dx="4">▪</tspan><tspan dx="6">Access Control</tspan></text>
    <text class="services" x="458" y="588" font-size="13">Cabling &amp; Networking <tspan dx="4">▪</tspan><tspan dx="6">Audio / Visual</tspan></text>
    <text class="contact" x="540" y="628" font-size="11.5">www.copperridgenet.example</text>
    <text class="contact" x="336" y="656" font-size="24">800-362-5914</text>
  </g>

  <!-- Front -->
  <g class="front-view">
    <path class="van-body" d="M880,60 Q884,44 905,44 L1100,44 Q1121,44 1125,60 L1140,175 L1148,360 L862,360 L868,175 Z"/>
    <path class="glass" d="M900,90 L1105,90 L1115,170 L890,170 Z" opacity="0.35"/>
    <rect class="van-body" x="852" y="148" width="24" height="40" rx="6"/>
    <rect class="van-body" x="1130" y="148" width="24" height="40" rx="6"/>
    <text class="services" x="1003" y="71" font-size="7.5" text-anchor="middle">Cameras ▪ Access Control</text>
    <text class="services" x="1003" y="80" font-size="7.5" text-anchor="middle">Cabling &amp; Networking ▪ Audio / Visual</text>
    <rect class="brand-mark" x="962" y="189" width="20" height="20"/>
    <text class="brand-name" x="992" y="202" font-size="11">COPPER RIDGE</text>
    <text class="brand-name" x="993" y="208.5" font-size="4" letter-spacing="2.2">TECHNOLOGIES</text>
    <text class="contact" x="992" y="215" font-size="4.6" style="fill:var(--white)">www.copperridgenet.example</text>
  </g>

  <!-- Rear -->
  <g class="rear-view">
    <path class="van-body" d="M880,440 Q884,424 905,424 L1120,424 Q1140,424 1144,440 L1150,690 L1150,775 L868,775 L868,690 Z"/>
    <rect class="band-silver" x="878" y="586" width="266" height="5"/>
    <rect class="band-blue" x="878" y="591" width="266" height="81"/>
    <g class="chip-blue">
      <rect x="1068" y="430" width="12" height="8"/><rect x="1086" y="432" width="10" height="10"/>
      <rect x="1104" y="434" width="14" height="14"/><rect x="1126" y="438" width="14" height="16"/>
      <rect x="1094" y="448" width="10" height="10"/><rect x="1112" y="456" width="16" height="14"/>
      <rect x="1090" y="462" width="10" height="8"/><rect x="1132" y="460" width="10" height="22"/>
      <rect x="1108" y="474" width="10" height="10"/>
    </g>
    <g class="chip-dark">
      <rect x="884" y="614" width="10" height="12"/><rect x="896" y="630" width="14" height="14"/>
      <rect x="884" y="646" width="10" height="12"/><rect x="912" y="646" width="10" height="10"/>
      <rect x="898" y="660" width="12" height="10"/><rect x="924" y="660" width="10" height="10"/>
      <rect x="912" y="632" width="8" height="8"/>
    </g>
    <rect class="brand-mark" x="980" y="454" width="60" height="60"/>
    <text class="brand-name" x="1011" y="541" font-size="24" text-anchor="middle">COPPER RIDGE</text>
    <text class="brand-name" x="1011" y="553" font-size="7.5" letter-spacing="3.6" text-anchor="middle">TECHNOLOGIES</text>
    <text class="services" x="1011" y="567" font-size="10" text-anchor="middle">Cameras ▪ Access Control</text>
    <text class="services" x="1011" y="579" font-size="10" text-anchor="middle">Cabling &amp; Networking ▪ Audio / Visual</text>
    <text class="contact" x="1013" y="638" font-size="20" text-anchor="middle">800-362-5914</text>
    <text class="contact" x="1013" y="653" font-size="9" text-anchor="middle">www.copperridgenet.example</text>
  </g>
</svg>
</div>
</body>
</html>
```